Bright Harbor Construction

We are a commercial construction company specializing in steel stud framing, drywall, taping and acoustical ceilings. We would like a company logo (Something that looks great and isnt boring) as we have not been able to come up with one. A modern looking card would definitely suit our personalities best

We would like to try and avoid using dark colors. I have learned from experience that dark colors are the last to looked at. Thank you

```html
<!DOCTYPE html>
<html lang="en">
<head>
<meta charset="utf-8">
<title>Bright Harbor Construction – Business Card</title>
<link rel="stylesheet" href="https://fonts.googleapis.com/css2?family=Montserrat:wght@400;500;700&display=swap">
<style>
  :root {
    --backdrop: #e9e9e9;
    --card-base: #ffffff;
    --card-band: #eef1f4;
    --accent: #ffc400;
    --accent-deep: #ff9800;
    --accent-light: #ffe08a;
    --name-colour: #f0a400;
    --text-main: #3a3a3a;
    --text-muted: #6b6b6b;
    --mark-colour: #4a4f57;
    --icon-ink: #ffffff;
  }
  * { margin: 0; padding: 0; box-sizing: border-box; }
  html, body { width: 1200px; height: 900px; overflow: hidden; }
  body {
    background: var(--backdrop);
    font-family: "Montserrat", sans-serif;
    position: relative;
  }
  .card {
    position: absolute;
    top: 150px;
    width: 366px;
    height: 600px;
    background: var(--card-base);
    overflow: hidden;
    box-shadow: -8px 8px 14px rgba(0, 0, 0, 0.12);
  }
  .card--front { left: 186px; }
  .card--back { left: 651px; }
  .card__shapes { position: absolute; inset: 0; width: 100%; height: 100%; }

  .brand {
    position: absolute;
    display: flex;
    align-items: center;
    gap: 10px;
    color: var(--mark-colour);
    font-weight: 500;
  }
  .brand__dot {
    flex: none;
    border-radius: 50%;
    background: var(--accent);
  }
  .brand--front { left: 36px; top: 36px; font-size: 19px; line-height: 1.05; }
  .brand--front .brand__dot { width: 34px; height: 34px; }

  .identity { position: absolute; right: 89px; top: 218px; text-align: right; }
  .identity__name {
    color: var(--name-colour);
    font-weight: 700;
    font-size: 23px;
    letter-spacing: -0.3px;
  }
  .identity__role {
    margin-top: 6px;
    margin-right: -9px;
    color: var(--text-muted);
    font-weight: 700;
    font-size: 16px;
  }

  .contacts { position: absolute; left: 0; top: 370px; list-style: none; }
  .contacts__item {
    display: flex;
    align-items: center;
    gap: 13px;
    height: 35.5px;
    color: var(--text-main);
    font-size: 19px;
  }
  .contacts__item:nth-child(1) { margin-left: 51px; }
  .contacts__item:nth-child(2) { margin-left: 60px; }
  .contacts__item:nth-child(3) { margin-left: 69px; }
  .contacts__item:nth-child(4) { margin-left: 78px; }
  .contacts__icon { width: 24px; height: 24px; flex: none; }

  .brand--back {
    left: 0; right: 0; top: 264px;
    flex-direction: column;
    gap: 8px;
    text-align: center;
    font-size: 25px;
    line-height: 1.1;
    color: var(--mark-colour);
  }
  .brand--back .brand__dot { width: 36px; height: 36px; }
  .back__web {
    position: absolute;
    right: 12px;
    top: 552px;
    color: var(--name-colour);
    font-weight: 500;
    font-size: 19px;
  }
</style>
</head>
<body>

<section class="card card--front" aria-label="Business card front">
  <svg class="card__shapes" viewBox="0 0 610 1000" preserveAspectRatio="none" aria-hidden="true">
    <defs>
      <linearGradient id="accentFill" x1="0" y1="0" x2="0" y2="1">
        <stop offset="0" stop-color="#ffd000"/>
        <stop offset="1" stop-color="#ffa000"/>
      </linearGradient>
    </defs>
    <polygon points="0,0 610,0 610,275 0,167" fill="var(--card-band)"/>
    <polygon points="495,255 610,275 610,770" fill="url(#accentFill)"/>
    <polygon points="495,255 510,258 610,700 610,770" fill="var(--accent-deep)"/>
    <polygon points="520,262 528,264 610,620 610,660" fill="var(--accent-light)" opacity="0.8"/>
    <polygon points="0,485 135,1000 0,1000" fill="url(#accentFill)"/>
    <polygon points="0,485 135,1000 122,1000 0,530" fill="var(--accent-light)"/>
    <polygon points="0,540 110,1000 98,1000 0,590" fill="var(--accent-deep)" opacity="0.6"/>
  </svg>

  <div class="brand brand--front">
    <span class="brand__dot"></span>
    <span class="brand__name">Bright Harbor<br>Construction</span>
  </div>

  <div class="identity">
    <p class="identity__name">YOUR NAME</p>
    <p class="identity__role">POSITION</p>
  </div>

  <ul class="contacts">
    <li class="contacts__item">
      <svg class="contacts__icon" viewBox="0 0 24 24" aria-hidden="true">
        <circle cx="12" cy="12" r="12" fill="var(--accent)"/>
        <path d="M7 15.5c2 2.5 4 3 5 2.5l1.3-1.3-1.8-1.6-1 .8c-.9-.5-1.8-1.4-2.3-2.3l.8-1-1.6-1.8L6.1 12c-.4 1 .2 2.5.9 3.5z" fill="var(--icon-ink)"/>
        <path d="M11 13l5-5" stroke="var(--icon-ink)" stroke-width="1.6"/>
      </svg>
      <span>+000 1234567</span>
    </li>
    <li class="contacts__item">
      <svg class="contacts__icon" viewBox="0 0 24 24" aria-hidden="true">
        <circle cx="12" cy="12" r="12" fill="var(--accent)"/>
        <rect x="5.5" y="8" width="13" height="8.5" rx="1" fill="none" stroke="var(--icon-ink)" stroke-width="1.4"/>
        <path d="M5.5 8.5l6.5 5 6.5-5M5.5 16l4.5-4M18.5 16L14 12" fill="none" stroke="var(--icon-ink)" stroke-width="1.2"/>
      </svg>
      <span>hello@bhconstruct.com</span>
    </li>
    <li class="contacts__item">
      <svg class="contacts__icon" viewBox="0 0 24 24" aria-hidden="true">
        <circle cx="12" cy="12" r="12" fill="var(--accent)"/>
        <g fill="none" stroke="var(--icon-ink)" stroke-width="1.1">
          <circle cx="12" cy="12" r="6.5"/>
          <ellipse cx="12" cy="12" rx="3" ry="6.5"/>
          <path d="M5.5 12h13M6.5 8.8h11M6.5 15.2h11M12 5.5v13"/>
        </g>
      </svg>
      <span>www.bhconstruct.com</span>
    </li>
    <li class="contacts__item">
      <svg class="contacts__icon" viewBox="0 0 24 24" aria-hidden="true">
        <circle cx="12" cy="12" r="12" fill="var(--accent)"/>
        <path d="M12 19.5s-5-5-5-9a5 5 0 0 1 10 0c0 4-5 9-5 9z" fill="var(--icon-ink)"/>
        <circle cx="12" cy="10.5" r="2" fill="var(--accent)"/>
      </svg>
      <span>your address here</span>
    </li>
  </ul>
</section>

<section class="card card--back" aria-label="Business card back">
  <svg class="card__shapes" viewBox="0 0 610 1000" preserveAspectRatio="none">
    <defs>
      <linearGradient id="skylineFill" x1="0" y1="0" x2="0" y2="1">
        <stop offset="0" stop-color="#dbe6f2"/>
        <stop offset="0.45" stop-color="#f3e6d6"/>
        <stop offset="0.75" stop-color="#e6dcd2"/>
        <stop offset="1" stop-color="#d9d3cd"/>
      </linearGradient>
    </defs>
    <polygon points="0,0 610,0 610,1000 0,1000" fill="var(--card-band)"/>
    <polygon role="img" aria-label="Photo of a city skyline with tall buildings at dusk"
             points="0,0 460,0 610,650 610,1000 150,1000 0,330" fill="url(#skylineFill)"/>
  </svg>

  <div class="brand brand--back">
    <span class="brand__dot"></span>
    <span class="brand__name">Bright Harbor<br>Construction</span>
  </div>

  <p class="back__web">www.bhconstruct.com</p>
</section>

</body>
</html>
```